Flyer for our prophetic church event

I need a flyer designed for the launching of our "7 Radiant Harvest Gatherings" event. This event should high light the next 7 Sundays starting on February the 11th, 2018

Event Name:
7 Radiant Harvests

Event Slogan or topic:
Go and tell John ... the blind see, the lame walk, the lepers are cleansed, the deaf hear, the dead are raised,
the poor have the gospel preached to them.

Speaker:
Prophet Marcus Obuya

February 11th
February 18th
February 25th
March 4th
March 11th
March 18th
March 25th

Location:
Talvor Community Center
382 Wendle Street
Portland, ME 04981
United States

Time:
10:00AM - 12:00PM

We welcome you all in the name of Jesus Christ

Contact Info:
Tel:+1(555) 302 1189 - Email:contact@mirovalefold.org - Website: http://velosa.org

Target Market(s)

Young adults

Industry/Entity Type

Church

Font styles to use
Other font styles liked:
• Surprise me, I trust the designers skills

Colors

Designer to choose colors to be used in the design.

Requirements
Must have
• The Velosa logo
• Marcus Obuya's picture
• The
Should not have
• The background of the Marcus Obuya's picture

```html
<!DOCTYPE html>
<html lang="en">
<head>
<meta charset="utf-8">
<title>7 Radiant Harvests – Flyer</title>
<link href="https://fonts.googleapis.com/css2?family=Cinzel:wght@400;600&family=Norican&family=Lato:wght@400;700&family=Tinos:wght@400;700&display=swap" rel="stylesheet">
<style>
:root{
  --navy:#0f3a66;
  --navy-deep:#0a2a4d;
  --gold:#f0c419;
  --gold-light:#fbe38a;
  --gold-dark:#c9a20d;
  --orange:#f7941d;
  --grey-band:#dcdcdc;
  --ink:#1c1c1c;
  --white:#ffffff;
  --strip:#333a42;
}
*{margin:0;padding:0;box-sizing:border-box}
html,body{width:806px;height:1200px;overflow:hidden;background:var(--white)}
.flyer{position:relative;width:806px;height:1200px;overflow:hidden;font-family:'Lato',sans-serif;color:var(--ink)}

.hero{position:absolute;left:0;top:0;width:806px;height:703px;
  background:radial-gradient(ellipse at 50% 45%,#1f4f80 0%,var(--navy) 45%,var(--navy-deep) 100%)}
.hero-shade{position:absolute;left:0;bottom:0;width:100%;height:160px;
  background:linear-gradient(to bottom,rgba(8,30,55,0),rgba(8,30,55,.55))}
.brand{position:absolute;top:70px;left:0;width:100%;text-align:center;
  font-family:'Cinzel',serif;font-size:58px;color:var(--white);letter-spacing:1px}
.brand-dot{display:inline-block;width:16px;height:16px;border-radius:50%;background:var(--orange);vertical-align:middle;margin-right:10px;position:relative;top:-6px}

.feature{position:absolute;left:229px;top:202px;width:340px;height:340px;border-radius:50%;
  border:3px solid var(--orange);padding:6px;background:var(--white)}
.feature-fill{width:100%;height:100%;border-radius:50%;
  background:radial-gradient(circle at 50% 55%,#f7a33c 0%,#e0691f 45%,#a8361a 80%,#3a1410 100%)}

.title{position:absolute;top:560px;left:0;width:100%;text-align:center;
  font-family:'Norican',cursive;font-size:66px;color:var(--white);line-height:1}
.subtitle{position:absolute;top:648px;left:0;width:100%;text-align:center;
  font-family:'Cinzel',serif;font-size:38px;color:var(--gold);letter-spacing:1.5px}

.welcome{position:absolute;top:703px;left:0;width:806px;height:48px;
  background:linear-gradient(90deg,var(--gold-dark),var(--gold) 30%,var(--gold-light) 60%,var(--gold) 85%,var(--gold-dark));
  font-family:'Cinzel',serif;font-weight:600;font-size:25px;color:var(--navy);text-align:center;line-height:48px;letter-spacing:.5px}

.theme{position:absolute;top:751px;left:0;width:806px;height:125px;background:var(--white)}
.theme-heading{position:absolute;right:38px;top:14px;font-family:'Norican',cursive;font-size:44px;color:var(--navy)}
.theme-verse{position:absolute;right:38px;top:74px;width:640px;text-align:right;font-size:14.5px;font-weight:700;line-height:20px;color:var(--ink)}

.dates{position:absolute;top:876px;left:0;width:806px;height:110px;background:var(--grey-band)}
.dates-row{position:absolute;left:290px;right:36px;display:flex;justify-content:space-between;color:var(--ink)}
.dates-row.major{top:22px;font-size:23px}
.dates-row.minor{top:66px;font-size:17px}
.dates sup{font-size:.55em}

.details{position:absolute;top:986px;left:0;width:806px;height:101px;background:var(--white)}
.time{position:absolute;left:310px;top:18px;display:flex;gap:14px;font-family:'Tinos',serif;font-size:28px;line-height:31px;color:var(--ink)}
.venue{position:absolute;left:488px;top:20px;display:flex;gap:14px}
.venue-text{font-family:'Tinos',serif;font-size:17px;line-height:22px;color:var(--ink)}
.venue-name{font-family:'Cinzel',serif;font-size:17px;letter-spacing:.5px}

.contact{position:absolute;top:1087px;left:0;width:806px;height:104px;
  background:linear-gradient(90deg,var(--gold-dark),var(--gold) 25%,var(--gold-light) 55%,var(--gold) 80%,var(--gold-dark))}
.contact-label{position:absolute;left:277px;top:26px;font-family:'Cinzel',serif;font-size:17px;color:var(--navy);text-decoration:underline}
.contact-line{position:absolute;left:277px;right:36px;top:60px;display:flex;justify-content:space-between;align-items:center;font-family:'Tinos',serif;font-weight:700;color:var(--navy-deep)}
.contact-item{display:flex;align-items:center;gap:6px}
.contact-item.phone{font-size:17px}
.contact-item.small{font-size:13px}
.bottom-strip{position:absolute;top:1191px;left:0;width:806px;height:9px;background:var(--strip)}

.speaker{position:absolute;left:17px;top:880px;width:276px;height:276px;border-radius:50%;
  border:3px solid var(--navy);overflow:hidden;background:var(--white);box-shadow:0 8px 14px rgba(0,0,0,.25)}
.speaker-photo{position:absolute;inset:0;background:radial-gradient(circle at 55% 40%,#e9e4de 0%,#cfc6bd 50%,#2b2b30 100%)}
.speaker-label{position:absolute;left:0;bottom:0;width:100%;height:72px;background:var(--navy);text-align:center;font-family:'Cinzel',serif;color:var(--white);padding-top:8px}
.speaker-role{font-size:11px;color:var(--gold)}
.speaker-name{font-size:13.5px;line-height:17px}
</style>
</head>
<body>
<div class="flyer">
  <section class="hero">
    <div class="hero-shade"></div>
    <div class="brand"><span class="brand-dot"></span>VELOSA</div>
    <div class="feature"><div class="feature-fill" role="img" aria-label="Wooden cross draped with purple cloth against an orange sunset sky"></div></div>
    <h1 class="title">7 Radiant Harvest</h1>
    <div class="subtitle">GATHERINGS</div>
  </section>

  <div class="welcome">WE WELCOME YOU ALL IN THE NAME OF JESUS CHRIST</div>

  <section class="theme">
    <div class="theme-heading">Go and tell John ...</div>
    <p class="theme-verse">the blind see, the lame walk, the lepers are cleansed, the deaf hear, the dead are raised, the poor have the gospel preached to them.</p>
  </section>

  <section class="dates">
    <div class="dates-row major"><span>February 11<sup>th</sup></span><span>February 18<sup>th</sup></span><span>February 25<sup>th</sup></span></div>
    <div class="dates-row minor"><span>March 4<sup>th</sup></span><span>March 11<sup>th</sup></span><span>March 18<sup>th</sup></span><span>March 25<sup>th</sup></span></div>
  </section>

  <section class="details">
    <div class="time">
      <svg width="18" height="18" viewBox="0 0 18 18" style="margin-top:4px"><circle cx="9" cy="9" r="9" fill="#f7941d"/><path d="M9 4v5h4" stroke="#fff" stroke-width="2" fill="none"/></svg>
      <div>10:00AM-<br>12:00PM</div>
    </div>
    <div class="venue">
      <svg width="14" height="20" viewBox="0 0 14 20" style="margin-top:2px"><path d="M7 0a7 7 0 0 0-7 7c0 5 7 13 7 13s7-8 7-13a7 7 0 0 0-7-7z" fill="#f7941d"/><circle cx="7" cy="7" r="2.6" fill="#fff"/></svg>
      <div class="venue-text"><div class="venue-name">TALVOR COMMUNITY CENTER</div>382 Wendle Street, Portland<br>ME 04981 United States</div>
    </div>
  </section>

  <section class="contact">
    <div class="contact-label">CONTACT US:</div>
    <div class="contact-line">
      <span class="contact-item phone"><svg width="14" height="14" viewBox="0 0 14 14"><path d="M3 1l2 3-1.5 1.5a8 8 0 0 0 5 5L10 9l3 2-1.5 2.5C6 13 1 8 .5 2.5z" fill="#0f3a66"/></svg>+1(555) 302 1189</span>
      <span class="contact-item small"><svg width="13" height="10" viewBox="0 0 13 10"><rect width="13" height="10" fill="#0f3a66"/><path d="M0 0l6.5 5L13 0" stroke="#f0c419" fill="none"/></svg>contact@mirovalefold.org</span>
      <span class="contact-item small"><svg width="12" height="12" viewBox="0 0 12 12"><circle cx="6" cy="6" r="5.3" stroke="#0f3a66" stroke-width="1.3" fill="none"/><path d="M.7 6h10.6M6 .7c-3 3-3 7.6 0 10.6M6 .7c3 3 3 7.6 0 10.6" stroke="#0f3a66" fill="none"/></svg>www.velosa.org</span>
    </div>
  </section>
  <div class="bottom-strip"></div>

  <div class="speaker">
    <div class="speaker-photo" role="img" aria-label="Portrait photo of the speaker, Prophet Marcus Obuya"></div>
    <div class="speaker-label">
      <div class="speaker-role">SPEAKER:</div>
      <div class="speaker-name">PROPHET<br>MARCUS OBUYA</div>
    </div>
  </div>
</div>
</body>
</html>
```